Zielgruppe
KLIVANTO gehört zu den führenden Online Marketing Agenturen in Europa. Wir unterstützen in ganz Europa Kunden bei der Umsetzung Ihrer Marketing- und Online-Vertriebsstrategien. Die Kunden reichen dabei von lokalen, kleinen Dienstleistern und Unternehmen bis hin zu multinationalen Konzernen.
www.klivanto.de | SEO AGENTUR | KLIVANTO
Aufgabenstellung
Im vorliegenden Projekt möchten wir eine Postkarte erstellen, die wir in jedem Restaurant, Einzelhandelsgeschäft oder auch auf Messen verteilen können.
Inhalt der Postkarte (Maxi quer 23,5cm x 12,5 cm, siehe Druckdaten) soll zum einen natürlich die Darstellung unserer Leistungen und des Unternehmensnamens sein. Also 'Online Marketing für Webseiten und Online-Shops'. Wir beraten Unternehmen generell auch vorab, welche Online Marketing Leistungen für das Unternehmen sinnvoll sind. Dazu gehören u.a.:
- Suchmaschinenoptimierung (SEO)
- Suchmaschinenwerbung/Vextra ads (SEA)
- Social Media Marketing (SMM)
- Online Marketing Strategieberatung (OMS)
Bei Rücksendung oder Meldung auf die Postkarte bieten wir eine kostenlose Webseitenanalyse mit Konkurrenzvergleich an, die sonst einen Wert von 499 Euro hätte.
Das ganze kostenlos und unverbindlich!
Es muss ein Feld angegeben sein, wo wir einen Gutscheincode eintragen können für die Gratisanalyse.
Zudem muss unsere Adresse aufgedruckt sein und das Feld für Briefmarke vorhanden sein.
Ziel muss es sein, dass sich die Unternehmer/Einzelhändler/Shop-Betreiber etc. bei uns melden, um diese Analyse zu bekommen. Das Ergebnis stellen wir dann vor Ort beim Kunden vor. (ebenfalls kostenlos)

```html
<!DOCTYPE html>
<html lang="de">
<head>
<meta charset="utf-8">
<title>KLIVANTO Postkarte</title>
<link href="https://fonts.googleapis.com/css2?family=Barlow+Semi+Condensed:wght@400;500;600;700&family=Bowlby+One&display=swap" rel="stylesheet">
<style>
:root{
  --backdrop:#b9b9b9;
  --sky-light:#6cbbdc;
  --sky-dark:#4a93b5;
  --crimson:#cc1640;
  --amber:#f5b13a;
  --ice:#a6dced;
  --field:#dbeef6;
  --ink:#1a1a1a;
  --grey-text:#555a5e;
  --stamp:#c7d4df;
  --white:#ffffff;
}
*{box-sizing:border-box;margin:0;padding:0}
html,body{width:1034px;height:1200px;overflow:hidden}
body{background:var(--backdrop);position:relative;font-family:"Barlow Semi Condensed",Arial,sans-serif}
.card{position:absolute;left:82px;width:869px;height:462px;background:var(--white);overflow:hidden;box-shadow:0 4px 10px rgba(0,0,0,.25)}
.card--front{top:93px}
.card--back{top:644px}
.abs{position:absolute}
.stamp-text{font-family:"Bowlby One",Impact,sans-serif;line-height:1;white-space:nowrap}

/* front */
.hero{left:0;top:0;width:869px;height:370px;background:radial-gradient(ellipse at 45% 55%,#8a8f93 0%,#707478 22%,var(--sky-light) 42%,var(--sky-dark) 100%)}
.hero-question{left:22px;top:104px;font-size:31px;color:var(--crimson);transform:rotate(-16deg);transform-origin:left top}
.chevron{left:475px;top:90px}
.voucher-disc{left:522px;top:-25px;width:324px;height:324px;border-radius:50%;background:var(--crimson);text-align:center;color:var(--white)}
.voucher-disc > div{position:absolute;left:0;right:0;line-height:1;white-space:nowrap}
.voucher-title{top:50px;font-size:42px;font-weight:700;letter-spacing:1px}
.voucher-line{font-size:23px;font-weight:500;color:var(--amber)}
.voucher-line--top{top:103px}
.voucher-headline{top:129px;font-size:39px;font-weight:700;color:var(--ice)}
.voucher-line--mid{top:181px}
.voucher-line--value{top:207px}
.voucher-price{font-size:38px;font-weight:700;vertical-align:-5px;margin-left:4px}
.voucher-disc > .code-field{left:91px;right:auto;top:257px;width:142px;height:36px;background:var(--white);border-radius:5px;color:var(--ink);font-size:11px;font-weight:500;padding-top:4px}
.services{left:34px;top:397px;font-size:17.5px;line-height:21px;color:var(--grey-text)}
.brand-name{left:654px;top:394px;font-size:50px;font-weight:400;color:var(--grey-text);letter-spacing:1px;line-height:1}

/* back */
.banner{left:0;top:0;width:869px;height:186px;background:linear-gradient(90deg,var(--sky-light) 0%,#5aa9cc 60%,var(--sky-dark) 100%)}
.banner-portrait{left:230px;top:20px;width:300px;height:166px;border-radius:150px 150px 0 0;background:radial-gradient(ellipse at 50% 70%,#a7abae 0%,#6f7478 60%,rgba(80,90,96,0) 100%)}
.headline{left:18px;top:70px;font-size:38px;color:var(--crimson);transform:rotate(-13deg);transform-origin:left top;line-height:1.05}
.benefit{font-size:17px}
.benefit--position{left:510px;top:18px;color:var(--crimson);transform:rotate(9deg);text-align:center}
.benefit--visitors{left:465px;top:70px;color:var(--amber);transform:rotate(-8deg);text-align:center}
.benefit--customers{left:597px;top:88px;color:var(--amber);transform:rotate(-3deg)}
.benefit--revenue{left:527px;top:116px;color:var(--amber);transform:rotate(8deg)}
.benefit--success{left:640px;top:138px;color:var(--crimson);transform:rotate(-13deg)}
.chevron--red{left:418px;top:27px}
.stamp-box{left:763px;top:29px;width:77px;height:97px;background:var(--stamp);font-size:10px;color:var(--ink);text-align:center;padding-top:32px;line-height:15px}
.form{left:29px;top:201px;width:514px}
.form-row{height:29px;background:var(--field);margin-bottom:9px;font-size:15px;color:#333;padding:5px 0 0 8px}
.address{left:605px;top:248px;font-size:18px;font-weight:500;color:var(--ink);line-height:24px;font-style:normal}
.address-city{display:block;font-size:26px;margin-top:20px}
.footer-band{left:0;top:398px;width:869px;height:64px;background:linear-gradient(90deg,#5ea7c9,var(--sky-dark));color:var(--white);padding:9px 0 0 29px}
.footer-intro{font-size:15.5px}
.footer-contacts{display:flex;align-items:center;gap:11px;font-size:16px;font-weight:600;margin-top:2px;white-space:nowrap}
</style>
</head>
<body>

<section class="card card--front">
  <div class="abs hero" role="img" aria-label="Schwarzweißfoto einer Frau, die durch ein Fernglas schaut, vor blauem Hintergrund"></div>
  <div class="abs hero-question stamp-text">Wo bleiben<br>die Kunden?</div>
  <svg class="abs chevron" width="44" height="62" viewBox="0 0 44 62"><polygon points="0,0 18,0 44,31 18,62 0,62 26,31" fill="#ffffff"/></svg>
  <div class="abs voucher-disc">
    <div class="voucher-title">GUTSCHEIN</div>
    <div class="voucher-line voucher-line--top">für eine kostenlose</div>
    <div class="voucher-headline">Webseitenanalyse</div>
    <div class="voucher-line voucher-line--mid">mit Konkurrenzvergleich</div>
    <div class="voucher-line voucher-line--value">im Wert von <span class="voucher-price">499 €</span></div>
    <div class="code-field">Gutscheincode</div>
  </div>
  <p class="abs services">Online Marketing Agentur für Suchmaschinenwerbung (SEO),<br>Suchmaschinenwerbung (SEA, Vextra ads) und Social Media Marketing (SMM)</p>
  <div class="abs brand-name">klivanto</div>
</section>

<section class="card card--back">
  <div class="abs banner"></div>
  <div class="abs banner-portrait" role="img" aria-label="Schwarzweißfoto einer Frau, die mit beiden Händen über den Kartenrand schaut"></div>
  <div class="abs headline stamp-text">100% VEXTRA<br>OPTIMIERUNG</div>
  <svg class="abs chevron chevron--red" width="47" height="70" viewBox="0 0 47 70"><polygon points="0,0 20,0 47,35 20,70 0,70 27,35" fill="#cc1640"/></svg>
  <div class="abs benefit benefit--position stamp-text">HÖHERE<br>POSITIONIERUNG</div>
  <div class="abs benefit benefit--visitors stamp-text">MEHR<br>BESUCHER</div>
  <div class="abs benefit benefit--customers stamp-text">MEHR KUNDEN</div>
  <div class="abs benefit benefit--revenue stamp-text">MEHR UMSATZ</div>
  <div class="abs benefit benefit--success stamp-text">MEHR ERFOLG</div>
  <div class="abs stamp-box">Bitte<br>freimachen</div>

  <div class="abs form">
    <div class="form-row">Firma:</div>
    <div class="form-row">Ansprechpartner:</div>
    <div class="form-row">Tel.:</div>
    <div class="form-row">Mail:</div>
    <div class="form-row">Web:</div>
  </div>

  <address class="abs address">
    KLIVANTO<br>Online Marketing<br>Lerchenweg 12
    <span class="address-city">33602 Falkenried</span>
  </address>

  <div class="abs footer-band">
    <div class="footer-intro">Wir beraten Sie kostenlos und unverbindlich:</div>
    <div class="footer-contacts">
      <span>Tel: 0800 5550194</span>
      <svg width="10" height="16" viewBox="0 0 10 16"><polyline points="2,1 8,8 2,15" fill="none" stroke="#fff" stroke-width="3"/></svg>
      <span>Mobil: +49 (0) 1550 2846173</span>
      <svg width="10" height="16" viewBox="0 0 10 16"><polyline points="2,1 8,8 2,15" fill="none" stroke="#fff" stroke-width="3"/></svg>
      <span>www.klivanto.de/gratisanalyse</span>
      <svg width="10" height="16" viewBox="0 0 10 16"><polyline points="2,1 8,8 2,15" fill="none" stroke="#fff" stroke-width="3"/></svg>
      <span>gratisanalyse@klivanto.de</span>
    </div>
  </div>
</section>

</body>
</html>
```